Business card design needed

I am looking for a simple but elegant business card that has a professional and a classy look and feel about it. Must engage the persons attention.
I own and run multiple dental practices and offer basic to advanced dentistry.

Target Market(s)

people looking for dentists

Industry/Entity Type

Dental

Contact Information for Business Card

Dr. Tobias Hendrikson
K9L Dental
Your Smile My Passion
Brackenfield - 52 Pellinor Street Ph: 0749581624
Corvale - 14 Fenwyck Street Ph: 0749316785
Tarrinda - Shop 8 27 Tolbarn Drive Ph: 49628437
Email: th@k9ldental.com.au

Requirements
Must have
• Contact Details
QR codes for easy storage and website redirection
email and web address

```html
<!DOCTYPE html>
<html lang="en">
<head>
<meta charset="utf-8">
<title>K9L Dental – Business Card</title>
<link rel="stylesheet" href="https://fonts.googleapis.com/css2?family=Roboto:ital,wght@0,400;0,700;1,400&display=swap">
<style>
  :root {
    --backdrop: #bababa;
    --teal: #008e9f;
    --slate: #2f4350;
    --paper: #ffffff;
    --rule: rgba(255,255,255,0.9);
    --mark-tint: #d6eef1;
  }
  html, body {
    margin: 0;
    padding: 0;
    width: 1200px;
    height: 819px;
    overflow: hidden;
    background: var(--backdrop);
    font-family: "Roboto", Arial, sans-serif;
  }
  .card {
    position: absolute;
    left: 152px;
    top: 119px;
    width: 901px;
    height: 550px;
    border: 1px solid #222;
    background: var(--paper);
    display: flex;
  }
  .card-front {
    position: relative;
    width: 473px;
    height: 100%;
  }
  .brand-mark {
    position: absolute;
    left: 113px;
    top: 98px;
    width: 230px;
    height: 230px;
    border-radius: 50%;
    background: var(--mark-tint);
  }
  .brand-name {
    position: absolute;
    left: 0;
    width: 100%;
    top: 358px;
    text-align: center;
    font-size: 64px;
    font-weight: 700;
    color: var(--slate);
    line-height: 1;
  }
  .practitioner {
    position: absolute;
    left: 0;
    width: 100%;
    top: 442px;
    text-align: center;
    font-size: 26px;
    font-weight: 700;
    color: var(--teal);
    line-height: 1;
  }
  .card-contacts {
    position: relative;
    flex: 1;
    background: var(--teal);
    color: var(--paper);
  }
  .location,
  .online {
    position: absolute;
    left: 45px;
    width: 333px;
    text-align: right;
  }
  .location p,
  .online p { margin: 0; }
  .location-name {
    font-size: 25px;
    font-weight: 700;
    line-height: 34px;
  }
  .location-address {
    font-size: 24px;
    line-height: 36px;
  }
  .location-phone {
    font-size: 28px;
    font-weight: 700;
    line-height: 38px;
  }
  .label { color: var(--slate); font-weight: 700; }
  .divider {
    position: absolute;
    left: 45px;
    width: 333px;
    height: 0;
    border-top: 2px solid var(--rule);
  }
  .email {
    font-size: 24px;
    font-style: italic;
    line-height: 36px;
  }
  .email .label { font-style: italic; }
  .website {
    font-size: 27px;
    font-weight: 700;
    line-height: 38px;
  }
</style>
</head>
<body>
  <div class="card">
    <section class="card-front">
      <div class="brand-mark" aria-hidden="true"></div>
      <div class="brand-name">K9L Dental</div>
      <div class="practitioner">Dr. Tobias Hendrikson</div>
    </section>

    <section class="card-contacts">
      <div class="location" style="top:44px">
        <p class="location-name">Brackenfield</p>
        <p class="location-address">52 Pellinor Street,</p>
        <p class="location-phone"><span class="label">p:</span> (07) 4958 1624</p>
      </div>
      <div class="divider" style="top:165px"></div>

      <div class="location" style="top:175px">
        <p class="location-name">Corvale</p>
        <p class="location-address">14 Fenwyck Street</p>
        <p class="location-phone"><span class="label">p:</span> (07) 4931 6785</p>
      </div>
      <div class="divider" style="top:298px"></div>

      <div class="location" style="top:307px">
        <p class="location-name">Tarrinda</p>
        <p class="location-address">Shop 8 27 Tolbarn Drive</p>
        <p class="location-phone"><span class="label">p:</span> (07) 4962 8437</p>
      </div>
      <div class="divider" style="top:426px"></div>

      <div class="online" style="top:437px">
        <p class="email"><span class="label">e:</span> th@k9ldental.com.au</p>
        <p class="website">k9ldental.com.au</p>
      </div>
    </section>
  </div>
</body>
</html>
```